DOVR Business Card Design Project

Company Name: DOVR (Dove Operational Versatile Resources) JLT.
Office Address: Office No 218, Saffron Crest Tower, Palmera Bay Towers, Dubai, U.A.E
Company line of business:
1) Currently we have a POS solution for retail outlets like duty free shops, supermarkets, department stores etc... The solution is deployed in Harbor Gate Retail on 350 POS and in Coralline Port Retail on 100 POS. So our main line of business is the deployment of this solution in retail outlets locally or regionally. We have already deployed the solution in India and Australia.
2) Integration of other third party POS systems with an online credit authorization netwotk in the UAE. This will enable POS applications to connect directly to the acquiring banks without needing an EFT terminal like Paxoline or Tramodex. The credit card payment is completed at the POS.
3) Other solutions that are targeting retail outlets like mobile POS, queue busting solutions, stock taking solutions using hand held devices, transaction capture systems, etc...
4) Other IT services like support of call center solutions from Bramwell Systems and development of new solutions as per customer requirements.
We need a business card design for the company. We don't have any specific requirements and will eave up to the designers to come up with creative designs. At the moment we still don't have a letter head design and the only thing that we have is the company logo that we will upload shortly.
Updates
Dear All,
I just uploaded the logo source files. I am sorry for the delay.
Regards
Tarek Demirci
I would like the business cards to have the following details:
Company Tel No
Company Fax No
Company Website Address
Employee Name
Employee Title
Employee Mobile Number
Employee Email Address

```html
<!DOCTYPE html>
<html lang="en">
<head>
<meta charset="utf-8">
<title>DOVR Business Cards</title>
<link href="https://fonts.googleapis.com/css2?family=Jost:ital,wght@0,400;0,500;1,400&display=swap" rel="stylesheet">
<style>
  :root {
    --page: #ffffff;
    --silver-light: #fbfbfb;
    --silver-mid: #dcdcdc;
    --silver-dark: #b5b5b5;
    --ink: #2f2f2f;
    --ink-soft: #555555;
    --paper: #ffffff;
    --night-top: #4a4a4a;
    --night-bottom: #111111;
    --on-night: #f2f2f2;
    --accent: #1f7fd0;
    --edge: #d0d0d0;
  }
  html, body {
    margin: 0;
    padding: 0;
    width: 1200px;
    height: 785px;
    overflow: hidden;
    background: var(--page);
    font-family: "Jost", "Futura", sans-serif;
  }
  .canvas { position: relative; width: 1200px; height: 785px; }

  .card {
    position: absolute;
    overflow: hidden;
    border-radius: 22px;
    box-shadow: 0 2px 5px rgba(0,0,0,0.25);
  }
  .card--light {
    left: 58px; top: 31px; width: 642px; height: 325px;
    background: var(--paper);
    border: 1px solid var(--edge);
    box-sizing: border-box;
  }
  .card--dark {
    left: 529px; top: 418px; width: 616px; height: 338px;
    border-radius: 30px 22px 30px 22px;
    background: linear-gradient(180deg, var(--night-top), var(--night-bottom));
  }
  .card__band {
    position: absolute;
    left: 0; top: 0; right: 0;
    background: linear-gradient(180deg, var(--silver-light) 0%, var(--silver-mid) 70%, var(--silver-dark) 100%);
  }
  .card--light .card__band { height: 176px; }
  .card--dark .card__band { height: 182px; }

  .brand { position: absolute; display: flex; align-items: center; gap: 26px; }
  .card--light .brand { left: 150px; top: 48px; }
  .card--dark .brand { left: 160px; top: 30px; }
  .brand__dot { width: 88px; height: 88px; border-radius: 50%; background: var(--accent); }
  .brand__name {
    font-weight: 400;
    font-size: 96px;
    line-height: 1;
    letter-spacing: 2px;
    color: var(--ink);
  }

  .person { position: absolute; white-space: nowrap; }
  .card--light .person { left: 0; right: 0; top: 192px; text-align: center; }
  .card--dark .person { left: 33px; top: 190px; }
  .person__name { font-weight: 400; color: var(--ink); letter-spacing: 0.5px; line-height: 1.1; }
  .card--light .person__name { font-size: 34px; }
  .card--dark .person__name { font-size: 29px; }
  .person__title {
    font-size: 11px;
    font-style: italic;
    letter-spacing: 1px;
    color: var(--ink-soft);
    text-transform: uppercase;
    margin-top: 2px;
  }
  .card--dark .person__title { padding-left: 82px; }

  .contact { position: absolute; font-size: 10px; color: var(--ink-soft); line-height: 1.8; white-space: nowrap; }
  .card--light .contact { left: 42px; top: 265px; }
  .card--dark .contact { left: 44px; top: 260px; }
  .contact__label { display: inline-block; width: 100px; }

  .company {
    position: absolute;
    font-size: 10.5px;
    font-weight: 500;
    color: var(--ink);
    line-height: 1.35;
    white-space: nowrap;
  }
  .card--light .company { left: 497px; top: 262px; }
  .card--dark .company { left: 498px; top: 258px; }

  .card--dark .person__name,
  .card--dark .person__title,
  .card--dark .contact,
  .card--dark .company { color: var(--on-night); }
</style>
</head>
<body>
<main class="canvas">

  <article class="card card--light">
    <div class="card__band">
      <div class="brand">
        <span class="brand__dot"></span>
        <span class="brand__name">DOVR</span>
      </div>
    </div>
    <div class="person">
      <div class="person__name">SEBASTIAN KOWALIK</div>
      <div class="person__title">Job Description</div>
    </div>
    <div class="contact">
      <div><span class="contact__label">Mobile Number :</span>+97150001234</div>
      <div><span class="contact__label">Email Address :</span>s.kowalik@mailbox.com</div>
    </div>
    <div class="company">
      <div>04-123-4500</div>
      <div>04-123-4501</div>
      <div>www.dovr.ae</div>
    </div>
  </article>

  <article class="card card--dark">
    <div class="card__band">
      <div class="brand">
        <span class="brand__dot"></span>
        <span class="brand__name">DOVR</span>
      </div>
    </div>
    <div class="person">
      <div class="person__name">SEBASTIAN KOWALIK</div>
      <div class="person__title">Job Description</div>
    </div>
    <div class="contact">
      <div><span class="contact__label">Mobile Number :</span>+97150001234</div>
      <div><span class="contact__label">Email Address :</span>s.kowalik@mailbox.com</div>
    </div>
    <div class="company">
      <div>04-123-4500</div>
      <div>04-123-4501</div>
      <div>www.dovr.ae</div>
    </div>
  </article>

</main>
</body>
</html>
```